Business card and (possibly) logo

Hi - we need a new business card.
We have an existing logo that we quite like but we are open to options.
We are an architectural firm - we specialize in upmarket residential work and apartment blocks.
We are chasing a business card at present but also want to extensively update our website going forward to attract a much higher level of client / investor / developer.
Our current logo is black, grey and yellow and based on the sun/moon temples in Mexico.
We are open to variations.
We want to communicate professionalism, trust, quality.
Our website is www.korvalstudio.com.au - but note as above - we want to change the website as well to be a lot 'classier' and to appeal to a higher end market.

thanks

Target Market(s)

We are an architect firm - our target market is Developers and builders of high end houses and luxury apartment blocks. Also private home owners wanting to build excellent expensive houses. (ideally over $1m budgets)

Industry/Entity Type

Residential

Requirements
Must have
• Logo
Contact details;
Name
phone, mobile, email, web

```html
<!DOCTYPE html>
<html lang="en">
<head>
<meta charset="utf-8">
<title>Korval Studio – Business Card</title>
<link rel="stylesheet" href="https://fonts.googleapis.com/css2?family=Didact+Gothic&family=Cousine:wght@700&family=Parisienne&display=swap">
<style>
  :root {
    --bg: #1c1c1c;
    --card-edge: #f4f4f2;
    --yellow: #e4c44f;
    --yellow-light: #f3d86a;
    --square: #ecd98a;
    --ink-light: #fbf6e4;
    --sky-top: #7f9ac4;
    --sky-low: #c7c9c4;
    --stone: #b99c76;
  }
  * { margin: 0; padding: 0; box-sizing: border-box; }
  html, body { width: 1200px; height: 1000px; overflow: hidden; }
  body {
    background: var(--bg);
    position: relative;
    font-family: "Didact Gothic", sans-serif;
  }
  .card {
    position: absolute;
    top: 150px;
    width: 410px;
    height: 700px;
    background: var(--card-edge);
    padding: 16px;
  }
  .card--front { left: 150px; }
  .card--back { left: 640px; }
  .card__face {
    position: relative;
    width: 100%;
    height: 100%;
    overflow: hidden;
    background: linear-gradient(160deg, #ebcb58 0%, var(--yellow) 60%, #dcb944 100%);
  }

  /* Front */
  .brand-square {
    position: absolute;
    left: 89px; top: 110px;
    width: 200px; height: 200px;
    background: var(--square);
  }
  .brand-name {
    position: absolute;
    left: 0; right: 0; top: 340px;
    text-align: center;
    color: var(--ink-light);
    font-size: 44px;
    letter-spacing: 3px;
    line-height: 1.1;
  }
  .front-web {
    position: absolute;
    left: 0; right: 0; bottom: 28px;
    text-align: center;
    font-family: "Cousine", monospace;
    font-weight: 700;
    font-size: 14px;
    color: var(--ink-light);
    opacity: .8;
  }

  /* Back */
  .hero {
    position: absolute;
    left: 0; top: 0;
    width: 100%; height: 360px;
  }
  .holder {
    position: absolute;
    right: 26px; top: 305px;
    text-align: right;
    color: var(--ink-light);
  }
  .holder__name { font-size: 38px; letter-spacing: 1px; line-height: 1; }
  .holder__role {
    font-family: "Parisienne", cursive;
    font-size: 28px;
    margin-top: 2px;
  }
  .contact {
    position: absolute;
    left: 0;
    display: flex;
    align-items: center;
  }
  .contact--address { top: 410px; }
  .contact--phone { top: 520px; }
  .contact__badge {
    width: 90px; height: 90px;
    margin-left: -22px;
    border-radius: 50%;
    background: var(--ink-light);
    display: flex; align-items: center; justify-content: center;
    padding-left: 18px;
  }
  .contact__text {
    margin-left: 18px;
    font-family: "Cousine", monospace;
    font-weight: 700;
    font-size: 15px;
    line-height: 1.35;
    color: var(--ink-light);
  }
</style>
</head>
<body>

<section class="card card--front" aria-label="Card front">
  <div class="card__face">
    <div class="brand-square"></div>
    <div class="brand-name">KORVAL STUDIO</div>
    <div class="front-web">http://www.korvalstudio.com.au</div>
  </div>
</section>

<section class="card card--back" aria-label="Card back">
  <div class="card__face">
    <svg class="hero" viewBox="0 0 378 360" role="img" aria-label="Photograph of a modern luxury house at dusk" preserveAspectRatio="none">
      <defs>
        <linearGradient id="heroPhoto" x1="0" y1="0" x2="0" y2="1">
          <stop offset="0" stop-color="var(--sky-top)"/>
          <stop offset=".45" stop-color="var(--sky-low)"/>
          <stop offset=".75" stop-color="var(--stone)"/>
          <stop offset="1" stop-color="#8c7356"/>
        </linearGradient>
      </defs>
      <rect width="378" height="360" fill="url(#heroPhoto)"/>
      <polygon points="0,0 110,0 378,250 378,360 0,360" fill="var(--yellow-light)" opacity=".45"/>
      <polygon points="0,250 378,210 378,360 0,360" fill="#ebcb58"/>
    </svg>

    <div class="holder">
      <div class="holder__name">MARCUS DELANEY</div>
      <div class="holder__role">architect</div>
    </div>

    <div class="contact contact--address">
      <div class="contact__badge">
        <svg width="40" height="46" viewBox="0 0 40 46" aria-hidden="true">
          <path d="M20 43 C8 28 4 22 4 16 a16 16 0 0 1 32 0 c0 6 -4 12 -16 27z" fill="none" stroke="var(--yellow)" stroke-width="3"/>
          <circle cx="20" cy="16" r="6" fill="none" stroke="var(--yellow)" stroke-width="3"/>
        </svg>
      </div>
      <div class="contact__text">Suite 9, 42 - 48<br>Harbourview Parade,<br>Seacliff, WA 6027</div>
    </div>

    <div class="contact contact--phone">
      <div class="contact__badge">
        <svg width="32" height="48" viewBox="0 0 32 48" aria-hidden="true">
          <rect x="3" y="3" width="26" height="42" rx="3" fill="none" stroke="var(--yellow)" stroke-width="3"/>
          <line x1="3" y1="36" x2="29" y2="36" stroke="var(--yellow)" stroke-width="3"/>
          <line x1="10" y1="9" x2="22" y2="9" stroke="var(--yellow)" stroke-width="3"/>
        </svg>
      </div>
      <div class="contact__text">1300 61 28 45<br>0427 305 861</div>
    </div>
  </div>
</section>

</body>
</html>
```